Review Site Redesign

We have a rather ambitious goal to reinvent (redesign) the way bank financial review sites present information. In that respect, we’re looking for an innovative creative design.
As examples of what I would call bad or boring design please look at the following sites:
1. http://brisklend.example/se
2. http://vantorquay.example/se/privatlan
3. http://glimsworth.example/no
These are the traditional way these types of review sites are organized: dull and boring. I think we can do a lot better than that.
I need a site that will capture attention end engage the visitor; a site that will create a more interactive and less passive user experience.
Scope of work should also include logo font and additional content space for articles, FAQ, widgets, social media links, etc.

Not sure what to advise you as best format - maybe a flash or js carousel, gallery, wheel, logo image matrix, or something else.
Maybe some kind of interactive logo matrix such as this site: http://www.quarnibo.example/
Please apply your best creative mind work to this problem.
Also, please think about creative use of background images, stock photos, etc.
For logo font use can use URL “pellrowatt.example” as placeholder.

```html
<!DOCTYPE html>
<html lang="no">
<head>
<meta charset="utf-8">
<title>Pellrowatt – sammenlign lån</title>
<link href="https://fonts.googleapis.com/css2?family=Oswald:wght@300;400&family=PT+Sans+Narrow&display=swap" rel="stylesheet">
<style>
:root{
  --dark:#2a2a2a;
  --bar:#3a3a3a;
  --yellow:#f5b800;
  --page:#ffffff;
  --panel:#ececec;
  --widget:#dcdcdc;
  --ink:#222;
  --muted:#777;
  --hero-sky:#fafafa;
  --hero-mist:#eeeeec;
  --hero-grey:#dcdcda;
  --hero-warm:#d8c6b6;
  --hero-shirt:#f4f2f0;
}
*{margin:0;padding:0;box-sizing:border-box}
html,body{width:724px;height:1200px;overflow:hidden;background:var(--page)}
body{position:relative;font-family:"PT Sans Narrow",Arial,sans-serif;color:var(--ink)}
.abs{position:absolute}
.head-band{left:0;top:0;width:724px;height:414px;background:radial-gradient(ellipse at 50% 30%,#3a3a3a,#1e1e1e 75%)}
.top-arc{left:200px;top:-10px;width:324px;height:16px;border-radius:0 0 50% 50%;background:var(--yellow)}
.main-nav{left:237px;top:37px;width:427px;height:26px;background:var(--bar);border-radius:3px 3px 0 0}
.main-nav a{font-family:Oswald,sans-serif;font-weight:300;font-size:10px;color:#fff;text-decoration:none;position:absolute;top:7px;transform:translateX(-50%);white-space:nowrap}
.nav-pointer{left:245px;top:33px;width:0;height:0;border-left:5px solid transparent;border-right:5px solid transparent;border-top:5px solid var(--yellow)}
.hero{left:60px;top:63px;width:604px;height:279px;
  background:
    radial-gradient(ellipse 150px 130px at 78% 30%,rgba(216,198,182,.75),transparent 70%),
    radial-gradient(ellipse 140px 120px at 88% 75%,var(--hero-shirt),transparent 75%),
    radial-gradient(ellipse 90px 110px at 48% 70%,var(--hero-grey),transparent 75%),
    linear-gradient(100deg,var(--hero-sky) 0%,var(--hero-mist) 40%,#e6e4e1 62%,var(--hero-warm) 78%,var(--hero-shirt) 100%)}
.badge-tab{left:60px;top:49px;width:22px;height:14px;background:var(--yellow)}
.badge{left:81px;top:49px;width:113px;height:135px}
.badge-name{left:81px;top:142px;width:113px;text-align:center;font-family:Oswald,sans-serif;font-weight:300;font-size:10px;color:#fff}
.hero-title{left:71px;top:262px;font-family:Oswald,sans-serif;font-size:15px;line-height:18px;color:var(--yellow);text-transform:uppercase}
.hero-sub{left:71px;top:298px;font-family:Oswald,sans-serif;font-size:10.5px;line-height:14px;color:#222;text-transform:uppercase}
.dots{left:339px;top:346px;display:flex;gap:4px}
.dots i{width:6px;height:6px;border-radius:50%;background:var(--yellow);display:block}
.dots i:first-child{background:#666}
.tabs{left:60px;top:379px;width:604px;height:35px;display:flex;background:#f4f4f4;border-radius:4px 4px 0 0;overflow:hidden}
.tabs span{font-family:Oswald,sans-serif;font-size:10px;text-transform:uppercase;display:flex;align-items:center;justify-content:center;border-right:1px solid #ccc;color:#222}
.tabs .active{background:var(--yellow)}
.offer-table{left:60px;top:414px;width:604px;height:117px;background:linear-gradient(#4a4a4a,#3a3a3a);border-top:2px dotted #888}
.col-head{top:421px;font-family:Oswald,sans-serif;font-weight:300;font-size:10px;color:var(--yellow)}
.head-line{left:60px;top:436px;width:604px;border-top:1px solid #555}
.cell{top:442px;font-size:8.5px;line-height:13px;color:#eee}
.cell em{font-style:normal;color:var(--yellow)}
.lender-box{left:72px;top:456px;width:62px;height:39px;background:#fff;border-radius:3px;display:flex;align-items:center;justify-content:center;font-family:Oswald,sans-serif;font-size:11px;color:#222}
.cta{left:597px;top:451px;width:44px;height:44px;border-radius:50%;background:#2a2a2a;border:2px solid #5a5a5a;color:var(--yellow);font-family:Oswald,sans-serif;font-size:7px;display:flex;align-items:center;justify-content:center}
.side-arrow{top:452px;width:44px;height:46px;border-radius:50%;background:#bbb;display:flex;align-items:center;justify-content:center}
.content{left:60px;top:531px;width:604px;height:586px;background:var(--panel)}
.section-title{font-family:Oswald,sans-serif;font-size:13px;color:#222;text-transform:uppercase}
.rule{height:2px;background:linear-gradient(90deg,#ccc,transparent)}
.thumb{width:77px;height:77px}
.art-title{font-family:Oswald,sans-serif;font-weight:300;font-size:11px;color:#111}
.art-text{font-size:8.5px;line-height:14px;color:#333;width:297px}
.meta{font-size:8px;color:var(--muted)}
.dash{border-top:1px dashed #aaa}
.view-more{left:413px;top:798px;font-family:Oswald,sans-serif;font-size:9px;text-decoration:underline;color:#222}
.faq-q{font-family:Oswald,sans-serif;font-weight:300;font-size:11px;color:#111}
.faq-a{font-size:8.5px;line-height:14px;color:#333;width:300px}
.widget{left:466px;width:188px;background:var(--widget);display:flex;align-items:center;justify-content:center;font-family:Oswald,sans-serif;font-size:17px;color:var(--yellow)}
.footer{left:0;top:1096px;width:724px;height:104px;background:radial-gradient(ellipse at 50% 0,#3a3a3a,#1d1d1d 80%)}
.content-cap{left:60px;top:1096px;width:604px;height:21px;background:var(--panel);border-radius:0 0 3px 3px}
.foot-link{top:1131px;font-family:Oswald,sans-serif;font-weight:300;font-size:8.5px;color:#999;transform:translateX(-50%);white-space:nowrap}
.social{top:1124px;width:21px;height:21px;border-radius:50%;border:2px solid #666}
.copyright{left:0;top:1174px;width:724px;text-align:center;font-family:Oswald,sans-serif;font-weight:300;font-size:7px;color:#888}
</style>
</head>
<body>
<div class="abs head-band"></div>
<div class="abs top-arc"></div>

<nav class="abs main-nav">
  <a style="left:13px">HEM</a>
  <a style="left:83px">ALLT OM EKONOMI</a>
  <a style="left:183px">EKONOMI ORDBOK</a>
  <a style="left:260px">OM OSS</a>
  <a style="left:327px">KONTAKT</a>
  <a style="left:391px">FORUM</a>
</nav>
<div class="abs nav-pointer"></div>

<div class="abs hero" role="img" aria-label="Foto: et smilende par ser sammen på en bærbar datamaskin mot lys bakgrunn"></div>

<div class="abs badge-tab"></div>
<svg class="abs badge" viewBox="0 0 113 135">
  <defs><linearGradient id="badgeFill" x1="0" y1="0" x2="1" y2="0"><stop offset="0" stop-color="#9a9a9a"/><stop offset=".5" stop-color="#c8c8c8"/><stop offset="1" stop-color="#8a8a8a"/></linearGradient></defs>
  <path d="M0 0H113V102L56.5 135 0 102Z" fill="url(#badgeFill)"/>
  <circle cx="56.5" cy="55" r="24" fill="#f5b800"/>
</svg>
<div class="abs badge-name">Pellrowatt</div>

<div class="abs hero-title">Glimsworth sammenligner og<br>vurderer online lån.</div>
<div class="abs hero-sub">Formålet er, å gi deg som bruker muligheten for<br>å finne et lån, som passer til nettopp dine behov.</div>
<div class="abs dots"><i></i><i></i><i></i><i></i><i></i></div>

<div class="abs tabs">
  <span class="active" style="width:82px">Alle lån</span>
  <span style="width:72px">Smålån</span>
  <span style="width:99px">Store lån</span>
  <span style="width:104px">Forbrukslån</span>
  <span style="width:95px">Kredittkort</span>
  <span style="width:70px">Favorittlån</span>
  <span style="width:82px;border-right:0">Nyheter</span>
</div>

<div class="abs offer-table"></div>
<div class="abs col-head" style="left:92px">Lån</div>
<div class="abs col-head" style="left:152px">Informasjon</div>
<div class="abs col-head" style="left:305px">Beløp</div>
<div class="abs col-head" style="left:403px">Løpetid</div>
<div class="abs col-head" style="left:466px">Åpen for</div>
<div class="abs head-line"></div>
<div class="abs lender-box">Lendora</div>
<div class="abs cell" style="left:152px;width:145px">FORBRUKSLÅN. Petter fra Lendora hjelper deg med små og store lån. Eks 25.000, 29,33% eff., 25.000 o/5 år, geb. 785, tot. 44.878.<br><em>LES MER</em></div>
<div class="abs cell" style="left:305px">5.000 - 25.000</div>
<div class="abs cell" style="left:403px">1-5 år</div>
<div class="abs cell" style="left:466px;width:105px">Fylt 20 år. Fast inntekt. Ingen betalingsanm.</div>
<div class="abs cta">SØK HER</div>
<div class="abs side-arrow" style="left:20px"><svg width="10" height="12"><path d="M9 0V12L0 6Z" fill="#fff"/></svg></div>
<div class="abs side-arrow" style="left:660px"><svg width="10" height="12"><path d="M1 0V12L10 6Z" fill="#fff"/></svg></div>

<div class="abs content"></div>

<div class="abs section-title" style="left:69px;top:542px">Latest Articles</div>
<div class="abs rule" style="left:69px;top:562px;width:380px"></div>

<div class="abs thumb" style="left:69px;top:572px;background:linear-gradient(135deg,#e6352a,#c81e17)" role="img" aria-label="Annonse for lån med en smilende kvinne"></div>
<div class="abs art-title" style="left:151px;top:571px">Slik låner du penger</div>
<div class="abs art-text" style="left:151px;top:587px">Det er ekstremt lett å låne penger bare for å gjøre hverdagen litt søtere. Det kan gjøres i løpet av 5 minutter på hjemmesiden til låneutbyderne. Du trenger bare å fylle inn dine private opplysninger og kontoopplysninger, velge lånebeløp og hvordan du vil dele opp avdragene. Når der er gjort, kan du slappe av og lene deg tilbake mens du venter på at din søknad om å låne penger blir vurdert.</div>
<div class="abs meta" style="left:151px;top:649px">Author: admin &nbsp;&nbsp;|&nbsp;&nbsp; Posted in Slik låner du penger</div>
<div class="abs dash" style="left:69px;top:669px;width:380px"></div>

<div class="abs thumb" style="left:69px;top:684px;background:linear-gradient(160deg,#4db3e6,#1f8cc9)" role="img" aria-label="Annonse for forbrukslån"></div>
<div class="abs art-title" style="left:151px;top:683px">Slik låner du penger</div>
<div class="abs art-text" style="left:151px;top:699px">Det er ekstremt lett å låne penger bare for å gjøre hverdagen litt søtere. Det kan gjøres i løpet av 5 minutter på hjemmesiden til låneutbyderne. Du trenger bare å fylle inn dine private opplysninger og kontoopplysninger, velge lånebeløp og hvordan du vil dele opp avdragene. Når der er gjort, kan du slappe av og lene deg tilbake mens du venter på at din søknad om å låne penger blir vurdert.</div>
<div class="abs meta" style="left:151px;top:761px">Author: admin &nbsp;&nbsp;|&nbsp;&nbsp; Posted in Slik låner du penger</div>
<div class="abs dash" style="left:69px;top:782px;width:380px"></div>
<div class="abs view-more">VIEW MORE</div>

<div class="abs section-title" style="left:69px;top:834px">FAQs</div>
<div class="abs rule" style="left:69px;top:854px;width:380px"></div>

<div class="abs faq-q" style="left:69px;top:863px">Søk online hos en godkjent utbyder ?</div>
<div class="abs faq-a" style="left:69px;top:879px">Du kan søke om lån hos utbyderne over. Alle er godkjente til å drive med lånevirksomhet i Norge, så du kan være sikker på at du får et lån med ordentlige og rettferdige vilkår. Klikk på linken og søk online på utbydernes hjemmesider.</div>
<div class="abs dash" style="left:69px;top:929px;width:380px"></div>

<div class="abs faq-q" style="left:69px;top:942px">Søk online hos en godkjent utbyder ?</div>
<div class="abs faq-a" style="left:69px;top:958px">Du kan søke om lån hos utbyderne over. Alle er godkjente til å drive med lånevirksomhet i Norge, så du kan være sikker på at du får et lån med ordentlige og rettferdige vilkår. Klikk på linken og søk online på utbydernes hjemmesider.</div>
<div class="abs dash" style="left:69px;top:1008px;width:380px"></div>

<div class="abs faq-q" style="left:69px;top:1017px">Søk online hos en godkjent utbyder ?</div>
<div class="abs faq-a" style="left:69px;top:1033px">Du kan søke om lån hos utbyderne over. Alle er godkjente til å drive med lånevirksomhet i Norge, så du kan være sikker på at du får et lån med ordentlige og rettferdige vilkår. Klikk på linken og søk online på utbydernes hjemmesider.</div>

<div class="abs widget" style="top:541px;height:174px">WIDGETS</div>
<div class="abs widget" style="top:722px;height:172px">WIDGETS</div>
<div class="abs widget" style="top:900px;height:173px">WIDGETS</div>

<footer class="abs footer"></footer>
<div class="abs content-cap"></div>
<div class="abs foot-link" style="left:72px">HEM</div>
<div class="abs foot-link" style="left:145px">ALLT OM EKONOMI</div>
<div class="abs foot-link" style="left:238px">EKONOMI ORDBOK</div>
<div class="abs foot-link" style="left:314px">OM OSS</div>
<div class="abs foot-link" style="left:375px">KONTAKT</div>
<div class="abs foot-link" style="left:439px">FORUM</div>
<div class="abs social" style="left:527px"></div>
<div class="abs social" style="left:553px"></div>
<div class="abs social" style="left:580px"></div>
<div class="abs social" style="left:607px"></div>
<div class="abs copyright">COPYRIGHT © PELLROWATT 2012 · ALL RIGHTS RESERVED</div>
</body>
</html>
```